Bauzaun- und Gerüst-Banner für Sachverständigenbüro (Arbeitssicherheit & Brandschutz)
Zielgruppe
Dienstleistungen in den Bereichen Arbeitssicherheit und Brandschutz
Zielgruppe sind vorallem Bauunternehmen, aber auch andere Unternehmen sämtlicher Branchen, sowie Kommunen und Verbände, wie Velmora, BKT, etc.
Aufgabenstellung
Es sollen ein Bauzaun-Banner und ein Gerüst-Banner designed werden, dabei wäre mir wichtig, dass den Betrachter klar wird, dass wir nicht nur Baustellen-Koordination können. Wir sind seit 15 Jahren am Markt und oft meinen unsere Kunden/Auftraggeber, dass wir nur Arbeitssicherheit auf Baustellen machen. Das ist so nicht richtig, es ist zwar unser Hauptgewerk, aber können und machen noch ganz viele andere Dienstleistungen in den Bereichen Arbeitssicherheit und Brandschutz, wie da wären:
- Sicherheits- und Gesundheitsschutz-Koordination (SiGeKo)
- Probenahme, Ausschreibung und Koordination von Schadstoffsanierungen
- externe Fachkräfte für Arbeitssicherheit (Sifa)
- externe Brandschutzbeauftragte
- Brandschutzerziehung und -aufklärung
- Prüfservice für Anlagen und Betriebsmittel
Zudem haben wir 2023 noch eine Akademie gegründet (trelwin Akademie UG), in wir viele Seminare in den Bereichen Arbeitssicherheit und Brandschutz anbieten, wie:
- Fachkraft für Arbeitssicherheit (Sifa 3.0)
- Sicherheitsbeauftragte
- Brandschutzbeauftragte
- Brandschutzhelfer
- Feuerlöschtraining
- Evakuierungstraining
- Havarie-/Leckagetraining
- Train-the-Trainer Diisocyanate
- Anwenderschulung Diisocyanate
- Arbeitssicherheit für Azubis und ausbildende Betriebe

```html
<!DOCTYPE html>
<html lang="de">
<head>
<meta charset="utf-8">
<title>trelwin.de – Bauzaun-Banner</title>
<link rel="stylesheet" href="https://fonts.googleapis.com/css2?family=Jost:wght@400;500;600;700&display=swap">
<style>
  :root {
    --page-bg: #f2f2f2;
    --red-start: #e8172a;
    --red-end: #ee3e49;
    --brand-blue: #42549a;
    --white: #ffffff;
  }
  * { box-sizing: border-box; margin: 0; padding: 0; }
  html, body {
    width: 1200px;
    height: 900px;
    overflow: hidden;
    background: var(--page-bg);
    font-family: "Jost", sans-serif;
  }
  .banner {
    position: absolute;
    left: 20px;
    top: 157px;
    width: 1160px;
    height: 586px;
    display: flex;
  }
  .message-panel {
    position: relative;
    flex: 0 0 902px;
    background: linear-gradient(120deg, var(--red-start) 0%, var(--red-end) 100%);
    color: var(--white);
  }
  .headline {
    position: absolute;
    left: 62px;
    top: 38px;
    font-weight: 700;
    font-size: 128px;
    line-height: 128px;
    letter-spacing: -1px;
  }
  .subline {
    position: absolute;
    left: 60px;
    top: 448px;
    width: 820px;
    font-weight: 400;
    font-size: 27px;
    line-height: 35px;
  }
  .brand-panel {
    position: relative;
    flex: 1;
    background: var(--brand-blue);
    color: var(--white);
    text-align: center;
  }
  .brand-name {
    position: absolute;
    left: 0;
    right: 0;
    display: flex;
    align-items: center;
    justify-content: center;
    gap: 10px;
    font-weight: 500;
    font-size: 26px;
    line-height: 30px;
  }
  .brand-name .dot {
    width: 28px;
    height: 28px;
    border-radius: 50%;
    border: 3px solid var(--white);
  }
  .brand-office { top: 104px; }
  .brand-academy { top: 280px; }
  .academy-claim {
    position: absolute;
    left: 0;
    right: 0;
    top: 326px;
    font-size: 14px;
    font-weight: 400;
  }
  .web-address {
    position: absolute;
    left: 0;
    right: 0;
    top: 496px;
    font-weight: 600;
    font-size: 23px;
  }
</style>
</head>
<body>
  <div class="banner">
    <section class="message-panel">
      <h1 class="headline">Wir sichern<br>mehr als nur<br>Gerüste.</h1>
      <p class="subline">Bei uns bekommst du Arbeitssicherheit PLUS – von SiGeKo bis Feuerlöschtraining. Seit 15 Jahren alles im Griff!</p>
    </section>
    <aside class="brand-panel">
      <div class="brand-name brand-office"><span class="dot"></span>trelwin.de</div>
      <div class="brand-name brand-academy"><span class="dot"></span>trelwin Akademie</div>
      <p class="academy-claim">Hier entstehen Sicherheitsexperten!</p>
      <p class="web-address">www.trelwin.de</p>
    </aside>
  </div>
</body>
</html>
```